Web Design Project

I want customers to be able to book appointments to get their makeup done and make a deposit and also have a gallery where i put my portfolio images, i want it to be very simple yet elegant.

Target Market(s)

Women ranging from 18-40 that want to get their makeup done

Industry/Entity Type

Makeup

Font styles to use
Sans Serif
Decorative

Requirements
Nice to have
• easy scheduling option and option to pay service in full on website.

```html
<!DOCTYPE html>
<html lang="en">
<head>
<meta charset="utf-8">
<title>Lumelle — Makeup Artist</title>
<link href="https://fonts.googleapis.com/css2?family=Roboto+Condensed:wght@400;700&family=Roboto:wght@400;700&display=swap" rel="stylesheet">
<style>
:root{
  --pink:#e5097f;
  --blue:#2b9cb6;
  --ink:#2d2a29;
  --text:#555;
  --dark:#3b3431;
  --darker:#2b2624;
  --panel:#4a4340;
  --rule:#8a8a8a;
  --white:#fff;
}
*{margin:0;padding:0;box-sizing:border-box}
html,body{width:1200px;height:3553px;overflow:hidden}
body{background:var(--white);font-family:"Roboto",Arial,sans-serif;color:var(--text);position:relative}
.abs{position:absolute}
.cond{font-family:"Roboto Condensed","Arial Narrow",sans-serif}

/* top accent */
.accent{top:0;left:0;width:1200px;height:6px;background:linear-gradient(90deg,var(--pink) 0 40%,var(--blue) 40% 60%,var(--pink) 60% 80%,var(--blue) 80%)}

/* header */
.logo{left:95px;top:62px;font:700 50px/1 "Roboto Condensed",sans-serif;color:var(--ink);letter-spacing:1px}
.nav{left:554px;top:82px;display:flex;gap:28px;font:700 15px/1 "Roboto Condensed",sans-serif;color:var(--ink);list-style:none}
.nav .active{color:var(--pink)}
.search{left:1090px;top:80px}

/* hero */
.hero{left:0;top:148px;width:1200px;height:439px;background:radial-gradient(circle at 25% 40%,#6b5a55 0,#2a2430 35%,#141b2d 70%),#1a1d2e}
.hero-tag{background:var(--blue);color:var(--white);font-family:"Roboto Condensed",sans-serif;font-weight:700;text-align:center}
.tag-small{left:705px;top:267px;width:219px;height:50px;font-size:33px;line-height:50px}
.tag-large{left:607px;top:329px;width:498px;height:77px;font-size:52px;line-height:77px}
.btn-slant{background:var(--blue);color:var(--white);font:700 22px/50px "Roboto Condensed",sans-serif;text-align:center;clip-path:polygon(0 0,100% 0,92% 100%,8% 100%)}
.hero-btn{left:750px;top:424px;width:207px;height:42px;line-height:42px;font-size:20px}

/* section headings */
.heading{border:2px solid var(--ink);color:var(--ink);font:700 22px/1 "Roboto Condensed",sans-serif;letter-spacing:2px;display:flex;align-items:center;justify-content:center;background:var(--white)}
.heading.on-dark{border-color:var(--white);color:var(--white);background:transparent}

/* portfolio */
.intro{left:133px;top:755px;width:934px;text-align:center;font-size:13px;line-height:22px}
.portfolio-photo{top:865px;width:288px;height:385px}
.portfolio-btn{left:495px;top:1348px;width:210px;height:50px}

/* features */
.features{left:0;top:1508px;width:1200px;height:634px;background:var(--dark)}
.feature{width:320px;color:#ddd}
.feature-head{display:flex;align-items:center;gap:14px;color:var(--white);font:700 21px/1 "Roboto Condensed",sans-serif}
.num{width:38px;height:38px;background:var(--white);color:var(--ink);font-size:28px;display:flex;align-items:center;justify-content:center}
.feature p{font-size:13px;line-height:18px;margin-top:12px}
.more{display:block;font:700 14px/1 "Roboto Condensed",sans-serif;color:var(--white);margin-top:6px}

/* testimonial */
.client-photo{left:95px;top:2332px;width:284px;height:219px;background:linear-gradient(135deg,#c79a7a,#8a5e44 60%,#e8d7c9)}
.client-name{left:406px;top:2370px;font:700 17px/1 "Roboto Condensed",sans-serif;color:var(--ink)}
.short-rule{height:2px;width:50px;background:var(--ink)}
.client-quote{left:406px;top:2418px;width:520px;font-size:14px;line-height:22px}
.arrow-box{width:44px;height:44px;background:#ddd}
.divider{left:95px;top:2618px;width:1010px;height:2px;background:var(--rule)}

/* tweets / highlights */
.tweet-name{left:116px;top:2850px;font:700 16px/1 "Roboto Condensed",sans-serif;color:var(--ink)}
.tweet-text{left:116px;top:2896px;width:470px;font-size:13px;line-height:20px}
.tweet-by{left:116px;top:2990px;font-size:12px}
.tweet-by b{color:var(--ink)}
.tweet-rule{left:95px;top:3027px;width:521px;height:2px;background:var(--ink)}
.highlight-photo{left:679px;top:2809px;width:426px;height:216px;background:linear-gradient(120deg,#3a2c2a,#9b7a6a 45%,#e9ddd6)}

/* services */
.services{left:0;top:3090px;width:1200px;height:374px;background:var(--dark)}
.service{top:10px;width:337px;height:316px;background:var(--panel)}
.service-head{height:100px;color:var(--white);font:700 25px/100px "Roboto Condensed",sans-serif;text-align:center;letter-spacing:1px}
.service-head.pink{background:var(--pink)}
.service-head.blue{background:var(--blue)}
.service .short-rule{background:#ccc;margin:28px auto 0}
.service p{font-size:13px;line-height:19px;color:#eee;text-align:center;padding:12px 40px 0}
.outline-btn{display:block;width:136px;height:36px;margin:14px auto 0;border:2px solid var(--white);color:var(--white);font:700 14px/32px "Roboto Condensed",sans-serif;text-align:center}
.signup{display:flex;width:270px;margin:16px auto 0}
.signup span{flex:1;height:36px;background:var(--white)}
.signup b{width:64px;height:36px;border:2px solid var(--white);color:var(--white);font:700 14px/32px "Roboto Condensed",sans-serif;text-align:center}

/* footer */
.footer{left:0;top:3464px;width:1200px;height:89px;background:var(--darker);color:#ccc;font-size:13px}
.copy{left:95px;top:40px}
.copy b{color:var(--white)}
.foot-links{left:448px;top:40px;display:flex;gap:22px;list-style:none}
.social{left:920px;top:32px;display:flex;gap:10px}
.social span{width:26px;height:26px;display:block}
</style>
</head>
<body>
<div class="abs accent"></div>

<header>
  <div class="abs logo">LUMELLE</div>
  <ul class="abs nav">
    <li class="active">HOME</li><li>ABOUT ME</li><li>MY SERVICES</li><li>BLOG</li><li>FAQs</li><li>CONTACT</li>
  </ul>
  <svg class="abs search" width="18" height="18" viewBox="0 0 18 18"><circle cx="7" cy="7" r="5" fill="none" stroke="#2d2a29" stroke-width="2"/><line x1="11" y1="11" x2="16" y2="16" stroke="#2d2a29" stroke-width="2"/></svg>
</header>

<section>
  <div class="abs hero" role="img" aria-label="Evening photo of a made-up couple against blurred city lights"></div>
  <div class="abs hero-tag tag-small">DOLOREMQUE</div>
  <div class="abs hero-tag tag-large">IAM AUT ASPERNATUR</div>
  <div class="abs btn-slant hero-btn">READ MORE</div>
</section>

<section>
  <div class="abs heading" style="left:489px;top:661px;width:222px;height:53px">MY PORTFOLIO</div>
  <p class="abs intro">Every look begins with your skin, your features and the occasion ahead. Browse recent bridal, evening and editorial work below, then book a session that suits your day, whether you want a soft natural glow or a bold statement finish for camera.</p>
  <div class="abs portfolio-photo" style="left:124px;background:linear-gradient(160deg,#6b4631,#c59a80 55%,#f1e4dc)" role="img" aria-label="Portfolio portrait of a woman with soft bridal makeup"></div>
  <div class="abs portfolio-photo" style="left:456px;background:linear-gradient(160deg,#3a2a22,#b78c72 50%,#e6d6c8)" role="img" aria-label="Portfolio portrait of a woman in a knit scarf with natural makeup"></div>
  <div class="abs portfolio-photo" style="left:788px;background:linear-gradient(160deg,#5a4a3e,#cfb8a4 50%,#efe8df)" role="img" aria-label="Portfolio portrait of a woman with glamorous evening makeup"></div>
  <div class="abs btn-slant portfolio-btn">READ MORE</div>
</section>

<section class="abs features">
  <div class="abs heading on-dark" style="left:436px;top:83px;width:328px;height:53px">WHAT YOU CHOOSE ME</div>
  <div class="abs feature" style="left:95px;top:202px"><div class="feature-head"><span class="num">1</span>AMET VOLUPTATEM</div><p>Skin prep tailored to you, with long wearing products chosen to last from first photo to final dance.</p><span class="more">READ MORE</span></div>
  <div class="abs feature" style="left:450px;top:202px"><div class="feature-head"><span class="num">2</span>AMET VOLUPTATEM</div><p>Easy online booking lets you pick a date and time that fits your schedule in a few simple clicks.</p><span class="more">READ MORE</span></div>
  <div class="abs feature" style="left:806px;top:202px"><div class="feature-head"><span class="num">3</span>AMET VOLUPTATEM</div><p>Secure your slot with a deposit or pay in full online before the day so you can simply relax.</p><span class="more">READ MORE</span></div>
  <div class="abs feature" style="left:95px;top:409px"><div class="feature-head"><span class="num">4</span>AMET VOLUPTATEM</div><p>On location service for weddings, events and shoots, with a calm and tidy kit set up anywhere.</p><span class="more">READ MORE</span></div>
  <div class="abs feature" style="left:450px;top:409px"><div class="feature-head"><span class="num">5</span>AMET VOLUPTATEM</div><p>Trial sessions help us shape your perfect look together well ahead of the big day itself.</p><span class="more">READ MORE</span></div>
  <div class="abs feature" style="left:806px;top:409px"><div class="feature-head"><span class="num">6</span>AMET VOLUPTATEM</div><p>Clean, cruelty free products and hygienic tools are used for every single client, every time.</p><span class="more">READ MORE</span></div>
</section>

<section>
  <div class="abs heading" style="left:468px;top:2216px;width:261px;height:54px">WHAT THEY SAYS</div>
  <div class="abs client-photo" role="img" aria-label="Portrait of a happy client with wavy hair"></div>
  <div class="abs client-name">NORA VALE, 25 YO</div>
  <div class="abs short-rule" style="left:406px;top:2398px"></div>
  <p class="abs client-quote">My makeup looked flawless all night and felt light on my skin. Booking was simple, the deposit took a minute, and I felt truly beautiful on my birthday .....</p>
  <svg class="abs arrow-box" style="left:1007px;top:2335px" viewBox="0 0 44 44"><rect width="44" height="44" fill="#ddd"/><polyline points="26,14 18,22 26,30" fill="none" stroke="#fff" stroke-width="3"/></svg>
  <svg class="abs arrow-box" style="left:1058px;top:2335px" viewBox="0 0 44 44"><rect width="44" height="44" fill="#ddd"/><polyline points="18,14 26,22 18,30" fill="none" stroke="#fff" stroke-width="3"/></svg>
  <div class="abs divider"></div>
</section>

<section>
  <div class="abs heading" style="left:246px;top:2693px;width:231px;height:54px">RECENT TWEETS</div>
  <div class="abs heading" style="left:708px;top:2693px;width:285px;height:54px">HIGHLIGHTS PRODUCT</div>
  <svg class="abs arrow-box" style="left:516px;top:2809px" viewBox="0 0 44 44"><rect width="44" height="44" fill="#ddd"/><polyline points="26,14 18,22 26,30" fill="none" stroke="#fff" stroke-width="3"/></svg>
  <svg class="abs arrow-box" style="left:569px;top:2809px" viewBox="0 0 44 44"><rect width="44" height="44" fill="#ddd"/><polyline points="18,14 26,22 18,30" fill="none" stroke="#fff" stroke-width="3"/></svg>
  <div class="abs tweet-name">ELLA MARSH @ LUMELLE</div>
  <div class="abs short-rule" style="left:116px;top:2878px"></div>
  <p class="abs tweet-text">New autumn looks are live in the portfolio, with warm bronze lids and berry lips. Spring wedding dates are filling fast, so book early .....</p>
  <div class="abs tweet-by">retweeted by <b>Ida Reyes</b></div>
  <div class="abs tweet-rule"></div>
  <div class="abs highlight-photo" role="img" aria-label="Makeup artist applying powder to a client with a brush"></div>
</section>

<section class="abs services">
  <div class="abs service" style="left:95px">
    <div class="service-head pink">BOOK APPOINTMENTS</div>
    <div class="short-rule"></div>
    <p>Choose your service, date and time, and we will confirm your booking by email within a day.</p>
    <span class="outline-btn">READ MORE</span>
  </div>
  <div class="abs service" style="left:430px">
    <div class="service-head blue">MAKE A DEPOSIT</div>
    <div class="short-rule"></div>
    <p>Hold your date with a small deposit, or pay for the full service now and arrive ready to relax.</p>
    <span class="outline-btn">READ MORE</span>
  </div>
  <div class="abs service" style="left:767px">
    <div class="service-head pink">NEWSLETTER</div>
    <div class="short-rule"></div>
    <p>Join the list for beauty tips, new looks and open dates.</p>
    <div class="signup"><span></span><b>SEND</b></div>
    <p>We send one short letter a month and never share your email address.</p>
  </div>
</section>

<footer class="abs footer">
  <div class="abs copy">© 2014 <b>LUMELLE STUDIO</b>. ALL RIGHTS RESERVED.</div>
  <ul class="abs foot-links"><li>ABOUT US</li><li>TERM AND USE</li><li>PRIVACY POLICY</li><li>FAQS</li><li>CONTACT US</li></ul>
  <div class="abs social">
    <span style="background:#3b5998"></span><span style="background:#2fa8e0"></span><span style="background:#d63a2c"></span><span style="background:#1a7bb9"></span><span style="background:#cb2027"></span>
  </div>
</footer>
</body>
</html>
```